Garden Maintenance business card

I need a business card design for my new business "Silver Birch Garden Co". I do garden maintenance including lawns, turf lawn, pruning, hedging, water systems, anything related to the garden really (dont think i need to include any of that except garden maintenance)

Reason: narrowed it down and just showing my business partners the designs, cheers

Industry/Entity Type

Business

Requirements
Must have
• Must Have:
- ABN: XX XXX XXX XXX
Mobile phone number 00 0000000
email address xxxx.xxxxxx@gmail.com
Owner Name Xxxx xxxxxx
title: garden specialist possibly under name or something sounding professional
logo which has been submitted both with a background and one without, feel free to choose whichever one you like
business name

```html
<!DOCTYPE html>
<html lang="en">
<head>
<meta charset="utf-8">
<title>Silver Birch Garden Co – Business Card</title>
<link rel="stylesheet" href="https://fonts.googleapis.com/css2?family=Baloo+2:wght@700&display=swap">
<style>
  :root {
    --band-green: #3fa535;
    --band-light: #8fd24a;
    --band-dark: #2c7d27;
    --grass-deep: #24501c;
    --grass-mid: #3c7a2a;
    --grass-light: #5a9a3a;
    --photo-sky: #6f9a4c;
    --photo-hedge: #3f7a2b;
    --photo-branch: #8a8f72;
    --text-white: #ffffff;
    --logo-ring: #bfe86a;
  }
  * { margin: 0; padding: 0; box-sizing: border-box; }
  html, body { width: 1200px; height: 675px; overflow: hidden; background: #ffffff; }
  body { font-family: "Baloo 2", "Arial Rounded MT Bold", sans-serif; color: var(--text-white); }

  .card { position: relative; width: 1200px; height: 675px; overflow: hidden; }

  .grass-backdrop {
    position: absolute; inset: 0;
    background: radial-gradient(ellipse at 55% 55%, var(--grass-light) 0%, var(--grass-mid) 45%, var(--grass-deep) 100%);
  }

  .photo-strip { position: absolute; top: 0; left: 0; width: 1200px; height: 102px; display: flex; }
  .photo-strip .photo { height: 100%; }
  .photo--sprinkler { width: 420px; background: linear-gradient(180deg, #a9c58c 0%, var(--photo-sky) 45%, #4c7f30 100%); }
  .photo--pruning { width: 400px; background: linear-gradient(135deg, #b8b9a0 0%, var(--photo-branch) 50%, #5e7d45 100%); }
  .photo--hedge { width: 380px; background: linear-gradient(180deg, #5b9a3a 0%, var(--photo-hedge) 60%, #2d5e20 100%); }

  .title-band {
    position: absolute; top: 102px; left: 0; width: 1200px; height: 86px;
    background: linear-gradient(180deg, var(--band-light) 0 14%, var(--band-green) 14% 86%, var(--band-light) 86% 100%);
    display: flex; align-items: center; justify-content: center;
  }
  .title-band .business-title { font-size: 46px; line-height: 1; letter-spacing: 0.5px; padding-top: 6px; }

  .logo-mark {
    position: absolute; left: 88px; top: 240px; width: 240px; height: 290px;
    display: flex; flex-direction: column; align-items: center; justify-content: center; gap: 14px;
    text-align: center;
  }
  .logo-mark .logo-dot { width: 64px; height: 64px; border-radius: 50%; background: var(--logo-ring); }
  .logo-mark .logo-name { font-size: 34px; line-height: 1.05; color: var(--text-white); }

  .contact-details { position: absolute; left: 0; top: 0; }
  .contact-line { position: absolute; font-size: 43px; line-height: 1; white-space: nowrap; }
  .contact-line .label { display: inline-block; }
  .contact-line--name { left: 380px; top: 248px; }
  .contact-line--name .value { margin-left: 40px; }
  .contact-line--phone { left: 328px; top: 340px; }
  .contact-line--phone .value { margin-left: 40px; }
  .contact-line--abn { left: 390px; top: 432px; }
  .contact-line--abn .value { margin-left: 40px; }

  .email-band {
    position: absolute; left: 0; bottom: 0; width: 1200px; height: 76px;
    background: linear-gradient(180deg, var(--band-light) 0 12%, var(--band-green) 12% 100%);
    display: flex; align-items: center; justify-content: center;
  }
  .email-band .email { font-size: 46px; line-height: 1; padding-top: 8px; }
</style>
</head>
<body>
  <main class="card">
    <div class="grass-backdrop" role="img" aria-label="Close-up photograph of a lush green lawn"></div>

    <div class="photo-strip">
      <div class="photo photo--sprinkler" role="img" aria-label="Photograph of a lawn sprinkler watering grass"></div>
      <div class="photo photo--pruning" role="img" aria-label="Photograph of secateurs pruning a branch"></div>
      <div class="photo photo--hedge" role="img" aria-label="Photograph of a neatly trimmed hedge"></div>
    </div>

    <header class="title-band">
      <h1 class="business-title">Silver Birch Garden / &nbsp;Garden Specialist</h1>
    </header>

    <div class="logo-mark">
      <span class="logo-dot"></span>
      <span class="logo-name">Silver Birch<br>Garden Co</span>
    </div>

    <section class="contact-details">
      <p class="contact-line contact-line--name"><span class="label">Contact :</span><span class="value">Tom Harlow</span></p>
      <p class="contact-line contact-line--phone"><span class="label">Mobile phone no. :</span><span class="value">041 736 2950</span></p>
      <p class="contact-line contact-line--abn"><span class="label">ABN :</span><span class="value">48213907765</span></p>
    </section>

    <footer class="email-band">
      <p class="email">email address : birchgardening@gmail.com</p>
    </footer>
  </main>
</body>
</html>
```